Promotional brochure for educational consulting firm

Hi Designers!

Please do a 8.5 x 11 inch tri-fold brochure as well as a 8.5 x 11 inch half-fold brochure.  I appreciate black and white versions in addition to color.  Please take a look at my company's website for a better sense of the look and feel I am going for:  www.brightlarkedu.org

Thanks!

Industry/Entity Type

Consulting

Colors
3176b5
85abd2
fcfbfd

```html
<!DOCTYPE html>
<html lang="en">
<head>
<meta charset="utf-8">
<title>Brightlark Associates LLC – Tri-fold Brochure</title>
<link href="https://fonts.googleapis.com/css2?family=Questrial&family=Montserrat:wght@800&display=swap" rel="stylesheet">
<style>
  :root{
    --blue:#3176b5;
    --blue-light:#85abd2;
    --paper:#fcfbfd;
    --paper-shade:#ebebed;
    --ink:#222222;
    --ink-soft:#3a3a3a;
    --rule:#cfcfd3;
  }
  *{margin:0;padding:0;box-sizing:border-box}
  html,body{width:1200px;height:945px;overflow:hidden;background:#ffffff}
  body{font-family:"Questrial",sans-serif;color:var(--ink)}
  .brochure{position:relative;width:1200px;height:945px;
    background:radial-gradient(ellipse at 50% 45%,var(--paper) 40%,var(--paper-shade) 100%)}
  .panel{position:absolute;top:0;width:400px;height:945px}
  .panel--contact{left:0}
  .panel--inside{left:400px;border-left:1px solid var(--rule)}
  .panel--cover{left:800px;border-left:1px solid var(--rule)}
  .swooshes{position:absolute;left:0;top:0;width:1200px;height:945px;pointer-events:none}
  .photo{position:absolute}
  .photo--pencils{left:15px;top:61px;width:371px;height:280px;border-radius:50%;
    background:linear-gradient(135deg,#8a3b2a 0%,#d8305a 30%,#e8c23a 45%,#3a55c8 62%,#2ea84a 78%,#6a2a8a 100%)}
  .photo--kids-cheering{left:40px;top:355px;width:360px;height:310px;
    background:radial-gradient(ellipse at 55% 60%,#e8b98f 0%,#9fd3e6 45%,rgba(252,251,253,0) 75%)}
  .photo--kids-reading{left:26px;top:672px;width:350px;height:262px;
    background:radial-gradient(ellipse at 55% 50%,#e9b48e 0%,#e6cf5a 35%,#6e8fc2 58%,rgba(252,251,253,0) 78%)}
  .center{position:absolute;left:0;width:400px;text-align:center}
  .section-label{top:452px;font-size:18px;color:var(--blue-light);letter-spacing:.5px}
  .brand-mark{position:absolute;left:160px;width:80px;height:80px;border-radius:50%;background:var(--ink)}
  .brand-mark--contact{top:512px}
  .brand-mark--cover{top:64px;left:152px;width:96px;height:96px;background:var(--blue)}
  .brand-name{font-size:20px;font-variant:small-caps;letter-spacing:.5px}
  .brand-name--contact{top:604px;color:var(--ink)}
  .brand-name--cover{top:184px;color:var(--blue)}
  .brand-tag{font-size:12.5px;text-transform:uppercase;letter-spacing:.3px}
  .brand-tag--contact{top:629px;color:var(--ink)}
  .brand-tag--cover{top:211px;color:var(--blue)}
  .person{top:714px;font-size:21px;color:var(--blue)}
  .line{display:flex;justify-content:center;align-items:center;gap:6px}
  .line svg{flex:none}
  .phone{font-size:18px;font-weight:700;color:var(--ink)}
  .phone--contact{top:771px}
  .fax{top:810px;font-size:15px;color:var(--ink-soft)}
  .email{top:859px;font-size:15px;color:var(--ink-soft)}
  .web{top:894px;font-size:15px;color:var(--ink-soft)}
  .lead-in{top:94px;font-size:29px;color:var(--ink)}
  .headline{top:140px;font-family:"Montserrat",sans-serif;font-weight:800;font-size:58px;color:var(--ink);letter-spacing:1px}
  .phone--inside{top:857px;font-size:24px;font-family:"Montserrat",sans-serif;font-weight:800}
  .tagline{top:276px;font-size:29px;line-height:37px;color:var(--blue-light)}
</style>
</head>
<body>
<main class="brochure">

  <section class="panel panel--contact">
    <div class="photo photo--pencils" role="img" aria-label="Close-up photo of sharpened coloured pencils"></div>
  </section>

  <section class="panel panel--inside">
    <div class="photo photo--kids-cheering" role="img" aria-label="Photo of cheerful schoolchildren with backpacks raising their arms"></div>
  </section>

  <section class="panel panel--cover">
    <div class="photo photo--kids-reading" role="img" aria-label="Photo of three smiling children lying on the floor with an open book"></div>
  </section>

  <svg class="swooshes" viewBox="0 0 1200 945" aria-hidden="true">
    <path d="M0,372 C120,338 290,360 388,494 C292,402 140,392 0,412 Z" fill="var(--blue)"/>
    <path d="M0,448 C70,424 160,412 245,410 C150,424 70,444 0,472 Z" fill="var(--blue-light)"/>
    <path d="M400,595 C510,640 650,675 800,676 C975,676 1120,580 1200,470 L1200,556 C1120,650 960,708 800,712 C620,716 500,700 400,688 Z" fill="var(--blue)"/>
    <path d="M400,612 C520,650 640,662 870,648 C700,676 520,668 400,640 Z" fill="var(--blue-light)"/>
    <path d="M400,700 C560,722 760,724 900,700 C1030,678 1140,600 1200,520" fill="none" stroke="var(--blue-light)" stroke-width="3"/>
    <path d="M400,712 C580,732 780,730 920,706 C1050,684 1150,610 1200,540" fill="none" stroke="var(--blue-light)" stroke-width="1.5"/>
    <path d="M820,650 C980,610 1120,520 1200,370" fill="none" stroke="var(--blue-light)" stroke-width="2"/>
    <path d="M860,664 C1010,622 1140,540 1200,420" fill="none" stroke="var(--blue-light)" stroke-width="1.5"/>
  </svg>

  <section class="panel panel--contact">
    <p class="center section-label">CONTACT US</p>
    <div class="brand-mark brand-mark--contact"></div>
    <p class="center brand-name brand-name--contact">Brightlark Associates LLC</p>
    <p class="center brand-tag brand-tag--contact">Supporting schools &amp; school leaders</p>
    <p class="center person">Marisa Dale, Ed.D.</p>
    <p class="center line phone phone--contact">
      <svg width="16" height="16" viewBox="0 0 16 16"><circle cx="8" cy="8" r="7" fill="none" stroke="var(--blue)" stroke-width="1.3"/><path d="M6 4 L8 6 L7 7.5 Q8 9.5 9 10 L10.5 9 L12 11 L10.5 12.5 Q6 11 4.5 5.5 Z" fill="var(--blue)"/></svg>555.014.2290</p>
    <p class="center line fax">
      <svg width="14" height="14" viewBox="0 0 14 14"><rect x="1.5" y="6" width="11" height="6" fill="none" stroke="var(--blue)" stroke-width="1.2"/><rect x="4" y="1.5" width="6" height="4.5" fill="none" stroke="var(--blue)" stroke-width="1.2"/></svg>555.014.2291</p>
    <p class="center line email">
      <svg width="16" height="12" viewBox="0 0 16 12"><rect x="0.5" y="0.5" width="15" height="11" fill="var(--blue)"/><path d="M1 1 L8 7 L15 1" fill="none" stroke="#fff" stroke-width="1.2"/></svg>marisa@brightlarkedu.org</p>
    <p class="center line web">
      <svg width="13" height="13" viewBox="0 0 14 14"><circle cx="7" cy="7" r="6" fill="none" stroke="var(--blue)" stroke-width="1.3"/><path d="M1 7 H13 M7 1 V13 M7 1 Q3 7 7 13 M7 1 Q11 7 7 13" fill="none" stroke="var(--blue)" stroke-width="1"/></svg>www.brightlarkedu.org</p>
  </section>

  <section class="panel panel--inside">
    <p class="center lead-in">School leadership is</p>
    <h1 class="center headline">24/7/365</h1>
    <p class="center line phone phone--inside">
      <svg width="24" height="24" viewBox="0 0 16 16"><circle cx="8" cy="8" r="7" fill="none" stroke="var(--blue)" stroke-width="1.3"/><path d="M6 4 L8 6 L7 7.5 Q8 9.5 9 10 L10.5 9 L12 11 L10.5 12.5 Q6 11 4.5 5.5 Z" fill="var(--blue)"/></svg>555.014.2290</p>
    <p class="center line web">
      <svg width="13" height="13" viewBox="0 0 14 14"><circle cx="7" cy="7" r="6" fill="none" stroke="var(--blue)" stroke-width="1.3"/><path d="M1 7 H13 M7 1 V13 M7 1 Q3 7 7 13 M7 1 Q11 7 7 13" fill="none" stroke="var(--blue)" stroke-width="1"/></svg>www.brightlarkedu.org</p>
  </section>

  <section class="panel panel--cover">
    <div class="brand-mark brand-mark--cover"></div>
    <p class="center brand-name brand-name--cover">Brightlark Associates LLC</p>
    <p class="center brand-tag brand-tag--cover">Supporting schools &amp; school leaders</p>
    <p class="center tagline">Let’s work together<br>to take your school<br>to the next<br>level of excellence.</p>
  </section>

</main>
</body>
</html>
```